Business Card Design Project - The Kernel Harbor

Company Name - The Kernel Harbor

We need a unique logo and business cards

We are a team of experienced IT professionals who specialize in providing business value to organizations via the analysis and understanding the challenges of your particular organization. We focus on understanding the challenges first, and execute against your priorities partnering with your highly valued key resources.

Our extensive experience and focus on Agile delivery methodologies help our clients continuously improve and deliver quality solutions. Using this approach we will always deliver the greatest return on your investments.

Target Market(s)

Large organizations IT departments

Industry/Entity Type

Business

Font styles to use
Serif
Sans Serif

Requirements
Should not have
• no pictures

```html
<!DOCTYPE html>
<html lang="en">
<head>
<meta charset="utf-8">
<title>The Kernel Harbor – Business Card</title>
<link href="https://fonts.googleapis.com/css2?family=Open+Sans:wght@400;600;700&display=swap" rel="stylesheet">
<style>
  :root {
    --backdrop: #1b1b1b;
    --card: #fbfbfa;
    --band: #3d3d3d;
    --accent: #f28c1c;
    --ink: #2a2a2a;
    --bar-text: #e9e9e9;
  }
  html, body {
    margin: 0;
    width: 1200px;
    height: 757px;
    overflow: hidden;
    background: var(--backdrop);
    font-family: "Open Sans", Arial, sans-serif;
  }
  .business-card {
    position: absolute;
    left: 150px;
    top: 121px;
    width: 900px;
    height: 514px;
    background: var(--card);
    overflow: hidden;
  }
  .card-shapes {
    position: absolute;
    inset: 0;
  }
  .holder-name {
    position: absolute;
    left: 90px;
    top: 62px;
    margin: 0;
    font-size: 26px;
    font-weight: 700;
    color: var(--accent);
  }
  .holder-role {
    position: absolute;
    left: 90px;
    top: 98px;
    margin: 0;
    font-size: 19px;
    font-weight: 400;
    color: var(--ink);
  }
  .contact-line {
    position: absolute;
    left: 110px;
    margin: 0;
    font-size: 20px;
    font-weight: 400;
    color: var(--bar-text);
    line-height: 45px;
  }
  .contact-phone { top: 140px; }
  .contact-web   { top: 200px; left: 130px; }
  .contact-mail  { top: 260px; left: 130px; }
  .brand-name {
    position: absolute;
    left: 0;
    right: 0;
    top: 340px;
    height: 110px;
    margin: 0;
    display: flex;
    align-items: center;
    justify-content: center;
    font-size: 38px;
    font-weight: 700;
    letter-spacing: 2px;
    text-transform: uppercase;
    color: var(--accent);
  }
</style>
</head>
<body>
  <div class="business-card">
    <svg class="card-shapes" width="900" height="514" viewBox="0 0 900 514" aria-hidden="true">
      <!-- contact bars -->
      <polygon points="0,140 400,140 420,162 400,185 0,185" fill="var(--band)"/>
      <polygon points="0,200 420,200 440,222 420,245 0,245" fill="var(--band)"/>
      <polygon points="0,260 440,260 460,282 440,305 0,305" fill="var(--band)"/>
      <!-- accent chevrons -->
      <polyline points="418,134 448,162 418,190" fill="none" stroke="var(--accent)" stroke-width="6"/>
      <polyline points="438,194 468,222 438,250" fill="none" stroke="var(--accent)" stroke-width="6"/>
      <polyline points="458,254 488,282 458,310" fill="none" stroke="var(--accent)" stroke-width="6"/>
      <!-- brand band -->
      <rect x="0" y="340" width="900" height="110" fill="var(--band)"/>
    </svg>

    <h1 class="holder-name">Dara Quill</h1>
    <p class="holder-role">Manager</p>

    <p class="contact-line contact-phone">00 987 654 321 00</p>
    <p class="contact-line contact-web">www.kernelharbor.com</p>
    <p class="contact-line contact-mail">email:hello@kernelharbor.com</p>

    <p class="brand-name">The Kernel Harbor</p>
  </div>
</body>
</html>
```